Business Card Design

Stronger Living Compact for the Plains is a partnership of twenty different health organisations in the western suburbs of Melbourne, working together to improve the health of the local community. The western suburbs of Melbourne is one of the fastest growing and most culturally diverse populations in Australia and its communities have some of the poorest health outcomes in Australia.
Please see location for copy of the SLCP:
http://kvrt.com.au/fileadmin/filemount/pdf_files/SLCFTP_13_FINAL_JUNE_2012.pdf

Reason: Hello. I've extended the deadline because in the brief I made a confusing mention about a logo, but I actually meant the 'Stronger Living Compact for the Plains' jpg that I had already attached. Sorry about the confusion Thanks Fiona

Hello, Thanks for the designs I have already received. I have extended the deadline because I made a confusing reference to a logo in my brief, but I was talking about the 'Stronger Living Compact for the Plains' jpg I had already attached. There is no other logo for me to provide.

Thanks, Fiona

Target Market(s)

Health and state/local government managers and CEOs

Industry/Entity Type

Health

Contact Information for Business Card

Fiona Tremblay
Executive Officer
Stronger Living Compact for the Plains
Ph: 0438 592 614
Fiona.Tremblay@qn.org.au

Requirements
Must have
• logo and details as provided.
Would prefer matt finish
I can't see that logo has successfully attached so if it has not, please email or call me to follow up.

```html
<!DOCTYPE html>
<html lang="en">
<head>
<meta charset="utf-8">
<title>Stronger Living Compact for the Plains – Business Card</title>
<link rel="stylesheet" href="https://fonts.googleapis.com/css2?family=Lexend:wght@600&family=Noto+Sans:wght@700&display=swap">
<style>
  :root {
    --blue: #3a8bd0;
    --green: #bcda6a;
    --map-green: #e2efc4;
    --white: #ffffff;
    --page: #ffffff;
  }
  * { margin: 0; padding: 0; box-sizing: border-box; }
  html, body {
    width: 1200px;
    height: 945px;
    overflow: hidden;
    background: var(--page);
  }
  .canvas {
    position: relative;
    width: 1200px;
    height: 945px;
  }
  .card {
    position: absolute;
    top: 0;
    height: 945px;
    overflow: hidden;
  }

  /* Front (contact side) */
  .card-front {
    left: 0;
    width: 586px;
    background: var(--blue);
  }
  .front-frame {
    position: absolute;
    left: 0; top: 0;
    width: 586px; height: 514px;
    background: var(--green);
  }
  .front-panel {
    position: absolute;
    left: 44px; top: 44px;
    width: 508px; height: 470px;
    background: var(--blue);
  }
  .wordmark {
    font-family: "Lexend", "Trebuchet MS", sans-serif;
    font-weight: 600;
    color: var(--white);
    letter-spacing: -0.5px;
  }
  .front-wordmark {
    position: absolute;
    left: 120px; top: 96px;
    font-size: 40px;
    line-height: 45px;
  }
  .name-band {
    position: absolute;
    left: 0; top: 514px;
    width: 552px; height: 88px;
    background: var(--green);
  }
  .contact {
    font-family: "Noto Sans", Tahoma, sans-serif;
    font-weight: 700;
    color: var(--white);
    position: absolute;
    white-space: nowrap;
  }
  .contact-name {
    left: 70px; top: 536px;
    font-size: 40px;
    line-height: 46px;
  }
  .contact-title {
    left: 0; width: 586px; text-align: center;
    top: 614px;
    font-size: 25px;
  }
  .contact-phone {
    left: 25px; top: 774px;
    font-size: 27px;
  }
  .contact-email {
    left: 25px; top: 842px;
    font-size: 27px;
  }

  /* Back (identity side) */
  .card-back {
    left: 607px;
    width: 593px;
    background: var(--green);
  }
  .back-panel {
    position: absolute;
    left: 31px; top: 40px;
    width: 522px; height: 860px;
    background: var(--blue);
  }
  .back-wordmark {
    position: absolute;
    left: 142px; top: 98px;
    font-size: 66px;
    line-height: 72px;
  }
  .region-map {
    position: absolute;
    left: 89px; top: 537px;
    width: 414px; height: 328px;
  }
</style>
</head>
<body>
<main class="canvas">
  <section class="card card-front" aria-label="Business card contact side">
    <div class="front-frame"></div>
    <div class="front-panel"></div>
    <p class="wordmark front-wordmark">Stronger<br>Living<br>Compact<br>for the<br>Plains</p>
    <div class="name-band"></div>
    <p class="contact contact-name">Fiona Tremblay</p>
    <p class="contact contact-title">Executive Officer</p>
    <p class="contact contact-phone">Ph: 0438 592 614</p>
    <p class="contact contact-email">Fiona.Tremblay@qn.org.au</p>
  </section>

  <section class="card card-back" aria-label="Business card identity side">
    <div class="back-panel"></div>
    <p class="wordmark back-wordmark">Stronger<br>Living<br>Compact<br>for the<br>Plains</p>
    <svg class="region-map" viewBox="0 0 414 328" role="img" aria-label="Map of the western Melbourne region served by the partnership">
      <rect width="414" height="328" rx="18" fill="var(--map-green)"/>
    </svg>
  </section>
</main>
</body>
</html>
```